CSS design for a web application

We are currently building a web application in JAVA. The application uses a combination of a HTML template and CSS for the look and feel. We currenly have a very corporate look and feel for demo puposes, but we need to have some CSS designs that we can show to prospective customers. One of the functionalities of our application is the possibility to upload a customer's own (CSS) design in the application.

Our first customer is a high school in The Netherlands (12-18 year students) for children who are physically challenged. So the design should be easy to read, buttons should be easy to see, read and click and the different parts/texts on the website shouldn't be too close together. At the same time, we would like to avoid too much scrolling (especially horizontally). Go with a minimun screen resolution of 1024 x 768.

As our users are children, nice colours and other fun elements would be nice, while keeping a 'school like' appearance. Please use pictures and icons that our users will relate too. We want to communicate that our software is easy, fun and at the same time professional.

Our product is based on Brindle Suite by Brindle and thus Brindle applications as Postrix, Calendar, Brindle Pages etc are all integrated in our software solution.

Find attached a static HTML file that contains our current CSS design. This should be used as a basis as it contains al the CSS elements that are used in the application. Please note that jQuery (javascript) knowledge is necessary.

Target Market(s)

Students at high school (age group 12/13 to 17/18). Users have physical disabilities that sometimes means they need special equipment/tools to operate their laptop.

Requirements
Must have
• Easy too navigate, buttons that are easy to see/use
Nice to have
• 'WOW' factor when people look at the design
Should not have
• buttons/text that is too small, too close together

```html
<!DOCTYPE html>
<html lang="nl">
<head>
<meta charset="utf-8">
<title>Study Guide Engels – Skyvane</title>
<link rel="stylesheet" href="https://fonts.googleapis.com/css2?family=Lato:wght@400;700&family=Roboto+Slab:wght@700&display=swap">
<style>
:root{
  --teal:#80cbcc;
  --black:#0c0c0c;
  --header-grey:#ebebeb;
  --coral:#e86a69;
  --coral-dark:#c94e4d;
  --menu-grey:#7f948c;
  --menu-grey-dark:#5f756d;
  --sub-grey:#e6e6e6;
  --panel:#f5f3e3;
  --panel-inner:#e6e3cf;
  --bar:#ebebeb;
  --text:#1c1c1c;
  --title:#6a6a66;
  --teal-text:#5b9a97;
  --link-red:#dd6a60;
  --blue:#1f9bd4;
  --footer:#2a2826;
  --white:#fff;
}
*{box-sizing:border-box;margin:0;padding:0}
html,body{width:1200px;height:837px;overflow:hidden}
body{position:relative;background:var(--teal);font-family:"Lato",sans-serif;color:var(--text)}

.app-bar{position:absolute;left:0;top:0;width:1200px;height:41px;background:var(--black);display:flex;align-items:center;padding-left:50px;gap:26px}
.app-link{color:var(--white);font-weight:700;font-size:16px;display:flex;align-items:center;gap:6px;text-decoration:none}
.app-icon{width:18px;height:18px;border-radius:3px;background:#dcdcdc}
.app-icon.round{border-radius:50%}

.site-header{position:absolute;left:0;top:41px;width:1200px;height:117px;background:var(--header-grey)}
.brand{position:absolute;left:64px;top:44px;display:flex;align-items:center;gap:8px;font-weight:700;font-size:27px;color:#2a9fd6}
.brand-dot{width:24px;height:24px;border-radius:50%;border:3px solid #2a9fd6}

.account{position:absolute;left:762px;top:0;width:401px;height:80px;background:var(--coral);border-radius:0 0 6px 6px;box-shadow:0 2px 3px rgba(0,0,0,.25);color:var(--white);text-align:right;padding:12px 20px 0 0}
.account-email{font-size:19px;font-weight:700;letter-spacing:.3px}
.account-actions{display:flex;justify-content:flex-end;gap:14px;margin-top:10px;font-size:17px;color:#2a2a2a}
.account-actions span{display:flex;align-items:center;gap:5px}
.account-actions i{width:15px;height:15px;border-radius:50%;background:rgba(255,255,255,.45);display:inline-block}

.search{position:absolute;left:764px;top:100px;width:399px;height:41px;border-radius:5px;background:#7fa79e;padding:3px;display:flex}
.search-label{background:#222;color:var(--white);font-weight:700;font-size:16px;letter-spacing:1px;width:82px;display:flex;align-items:center;justify-content:center;border-radius:3px 0 0 3px}
.search-field{flex:1;background:#f4f2df}
.search-go{background:#222;color:var(--white);font-weight:700;font-size:16px;width:44px;display:flex;align-items:center;justify-content:center;border-radius:0 3px 3px 0}

.sidebar{position:absolute;left:40px;top:158px;width:219px;height:545px;background:#ececec}
.menu-title{position:absolute;left:3px;top:2px;width:211px;height:40px;background:var(--coral);border-radius:3px;box-shadow:0 2px 2px rgba(0,0,0,.3);color:var(--white);font-family:"Roboto Slab",serif;font-weight:700;font-size:20px;display:flex;align-items:center;justify-content:center;letter-spacing:.5px}
.menu-item{position:absolute;left:7px;width:217px;height:31px;background:linear-gradient(var(--menu-grey),var(--menu-grey-dark));border-radius:3px;box-shadow:0 2px 2px rgba(0,0,0,.3);color:var(--white);font-size:18px;display:flex;align-items:center;justify-content:space-between;padding:0 12px 0 19px}
.menu-item svg{width:14px;height:18px}
.sub-item{position:absolute;left:7px;width:207px;height:32px;background:linear-gradient(#f2f2f2,var(--sub-grey));border-radius:3px;font-size:18px;color:#222;padding-left:60px;display:flex;align-items:center}

.content{position:absolute;left:279px;top:216px;width:887px;height:487px;background:var(--panel);border-radius:4px}
.page-title{position:absolute;left:16px;top:12px;font-family:"Roboto Slab",serif;font-weight:700;font-size:29px;color:var(--title)}
.content-inner{position:absolute;left:9px;top:51px;width:862px;height:427px;background:var(--panel-inner)}
.info-bar{position:absolute;left:6px;top:11px;width:858px;height:71px;background:var(--bar);border:1px solid #cfcfcf;border-radius:4px}
.back-btn{position:absolute;left:16px;top:25px;width:90px;height:25px;background:linear-gradient(#2aa6e0,#137cbb);border:1px solid #0f6aa0;border-radius:3px;color:var(--white);font-size:13px;font-weight:700;display:flex;align-items:center;justify-content:center}
.course-desc{position:absolute;left:148px;top:17px;width:400px;font-size:16px;font-weight:700;line-height:21px}
.course-meta{position:absolute;right:8px;top:17px;text-align:left;font-size:16px;font-weight:700;line-height:21px}
.course-meta .course-name{color:var(--blue)}

.assignments{position:absolute;left:4px;top:90px;width:861px;border-collapse:collapse;background:var(--white);border:1px solid #9a9a9a}
.assignments th{height:44px;background:linear-gradient(#fafafa,#e4e4e4);color:var(--teal-text);font-size:17px;font-weight:700;text-align:left;padding-left:14px;border-right:1px solid #c8c8c8;border-bottom:2px solid #b5b5b5}
.assignments th.center{text-align:center;padding-left:0}
.assignments td{height:61px;vertical-align:top;padding:9px 14px 0;font-size:15px;line-height:22px;border-right:1px solid #c8c8c8;border-bottom:1px solid #b5b5b5}
.assignments td.task{color:var(--link-red)}
.assignments td.date{text-align:center}
.col-task{width:134px}.col-desc{width:471px}.col-date{width:140px}

.site-footer{position:absolute;left:40px;top:729px;width:1126px;height:82px;background:var(--footer);border-top:6px solid #e2dfc6;display:flex;align-items:center;padding-left:23px;gap:12px;color:#cfcfcf;font-size:16px}
.footer-brand{display:flex;align-items:center;gap:6px;font-weight:700;font-size:20px;color:#7a7a7a}
.footer-brand .dot{width:18px;height:18px;border-radius:50%;border:2px solid #7a7a7a}
</style>
</head>
<body>

<nav class="app-bar">
  <a class="app-link"><span class="app-icon"></span>Postrix</a>
  <a class="app-link"><span class="app-icon"></span>Calendar</a>
  <a class="app-link"><span class="app-icon"></span>Documents</a>
  <a class="app-link"><span class="app-icon"></span>Sites</a>
  <a class="app-link"><span class="app-icon round"></span>Chat</a>
</nav>

<header class="site-header">
  <div class="brand"><span class="brand-dot"></span>skyvane</div>
</header>

<div class="account">
  <div class="account-email">student@lms.skyvane.nl</div>
  <div class="account-actions">
    <span><i></i>Settings</span>
    <span><i></i>Help</span>
    <span><i></i>Signout</span>
  </div>
</div>

<form class="search">
  <div class="search-label">SEARCH</div>
  <div class="search-field"></div>
  <div class="search-go">GO</div>
</form>

<aside class="sidebar">
  <div class="menu-title">MENU</div>
  <div class="menu-item" style="top:62px">Home<svg viewBox="0 0 14 18"><path d="M3 2l8 7-8 7" fill="none" stroke="#fff" stroke-width="3"/></svg></div>
  <div class="menu-item" style="top:104px">Study Guide<svg viewBox="0 0 14 18"><path d="M3 2l8 7-8 7" fill="none" stroke="#fff" stroke-width="3"/></svg></div>
  <div class="sub-item" style="top:145px">Germen</div>
  <div class="sub-item" style="top:187px">English</div>
  <div class="sub-item" style="top:229px">French</div>
  <div class="sub-item" style="top:271px">Economics</div>
  <div class="sub-item" style="top:313px">Dutch</div>
  <div class="sub-item" style="top:355px">Chemistry</div>
  <div class="menu-item" style="top:400px">Books<svg viewBox="0 0 14 18"><path d="M3 2l8 7-8 7" fill="none" stroke="#fff" stroke-width="3"/></svg></div>
  <div class="menu-item" style="top:442px">Tests<svg viewBox="0 0 14 18"><path d="M3 2l8 7-8 7" fill="none" stroke="#fff" stroke-width="3"/></svg></div>
  <div class="menu-item" style="top:484px">Results<svg viewBox="0 0 14 18"><path d="M3 2l8 7-8 7" fill="none" stroke="#fff" stroke-width="3"/></svg></div>
</aside>

<main class="content">
  <h1 class="page-title">Study Guide Engels</h1>
  <div class="content-inner">
    <div class="info-bar">
      <div class="back-btn">&lt;&lt;Back</div>
      <div class="course-desc">Engels door leraar@lms.skyvane.nl voor m2@lms.skyvane.nl</div>
      <div class="course-meta"><div class="course-name">English by Skyvane</div>Eerste trimester (22-12-2010)</div>
    </div>
    <table class="assignments">
      <thead>
        <tr><th class="col-task">Assignment</th><th class="col-desc">Description</th><th class="col-date center">Deadline</th><th class="center">Mark</th></tr>
      </thead>
      <tbody>
        <tr><td class="task">Opdracht 1</td><td>Engels opdracht 1 door leraar@lms.skyvane.nl voor m2@lms.skyvane.nl</td><td class="date">22-12-2010</td><td></td></tr>
        <tr><td class="task">Opdracht 2</td><td>Engels opdracht 1 door leraar@lms.skyvane.nl voor m2@lms.skyvane.nl</td><td class="date">22-12-2010</td><td></td></tr>
        <tr><td class="task">Opdracht 3</td><td>Engels opdracht 1 door leraar@lms.skyvane.nl voor m2@lms.skyvane.nl</td><td class="date">22-12-2010</td><td></td></tr>
        <tr><td></td><td></td><td></td><td></td></tr>
      </tbody>
    </table>
  </div>
</main>

<footer class="site-footer">
  Copyright © 2010-2011
  <span class="footer-brand"><span class="dot"></span>skyvane</span>
</footer>

</body>
</html>
```